Marlowick APP redesign and color change

I am looking for a new design for my app. Please see the attached current design.

Currently, I have a functioning app but the colors and design are awful!
The logo is great but the rest of the app needs a refresh.
(Logo hi res not yet available but will upload soon.)
New colors or anything that is cutting edge.

Basically: It is a secure social media app within a school system where the teachers, students and parents can text, exchange photos, plan curriculum, etc.

I NEED ONLY landing page with a new look!
Looking for one distinct design for the landing page with new look.
The developer will apply this one design towards the rest of the pages/app screens.

Because part of the social media I need the feel and look of what is now the trend. Something that will attract and keep the client(s) interested. I am really leaving all the creative work to the designer and open to any suggestions.
Updates

Target Market(s)

Schools, community, teachers, students, colleges, sport teams

Industry/Entity Type

Non Profit

Font styles to use
Serif
Sans Serif

Colors

Designer to choose colors to be used in the design.

Requirements
Must have
• Sharp, trendy, millennial feel
Nice to have
• Up to designer
Should not have
• Up to designer

```html
<!DOCTYPE html>
<html lang="en">
<head>
<meta charset="utf-8">
<title>Marlowick – Conversations</title>
<link href="https://fonts.googleapis.com/css2?family=Roboto:wght@400;500&display=swap" rel="stylesheet">
<style>
  :root {
    --stage: #bacbdb;
    --surface: #ffffff;
    --list-bg: #e8e8e8;
    --divider: #dcdcdc;
    --ink: #1d1d1d;
    --muted: #8a8a8a;
    --icon-idle: #c9ced6;
    --icon-active: #5c87c9;
    --online: #3aa33a;
    --away: #c4c4c4;
    --busy: #e03a3a;
    --placeholder: #b9d5ea;
  }
  * { box-sizing: border-box; margin: 0; padding: 0; }
  html, body { width: 1200px; height: 675px; overflow: hidden; }
  body {
    background: radial-gradient(ellipse at 50% 60%, #a9b9c9 0%, var(--stage) 45%);
    font-family: "Roboto", Arial, sans-serif;
    position: relative;
  }
  .app-screen {
    position: absolute;
    left: 464px; top: 105px;
    width: 271px; height: 466px;
    background: var(--list-bg);
    border-radius: 7px;
    overflow: hidden;
    box-shadow: 0 40px 60px -10px rgba(70, 85, 105, .45);
  }
  .top-bar {
    height: 53px;
    background: var(--surface);
    display: flex; align-items: center; justify-content: center;
    position: relative;
  }
  .top-bar h1 { font-size: 13.5px; font-weight: 500; color: var(--ink); }
  .menu-icon { position: absolute; left: 13px; top: 19px; }
  .search-icon { position: absolute; right: 20px; top: 16px; }
  .conversation-list { list-style: none; }
  .conversation {
    height: 59.3px;
    display: flex; align-items: center;
    padding-left: 12px;
    border-bottom: 1px solid var(--divider);
  }
  .avatar {
    width: 40px; height: 40px; border-radius: 50%;
    flex: none; margin-right: 8px;
    border: 1.5px solid #fff;
  }
  .avatar--placeholder {
    background: var(--placeholder);
    display: flex; align-items: center; justify-content: center;
  }
  .contact-name { font-size: 13px; color: var(--ink); line-height: 16px; }
  .last-message {
    font-size: 8.6px; color: var(--muted);
    display: flex; align-items: center; gap: 4px; margin-top: 1px;
  }
  .status { width: 4.5px; height: 4.5px; border-radius: 50%; }
  .status--online { background: var(--online); }
  .status--away { background: var(--away); }
  .status--busy { background: var(--busy); }
  .tab-bar {
    position: absolute; left: 0; bottom: 0;
    width: 100%; height: 44px;
    background: var(--surface);
    display: flex; justify-content: space-around; align-items: center;
    padding: 0 8px;
  }
</style>
</head>
<body>
  <main class="app-screen">
    <header class="top-bar">
      <svg class="menu-icon" width="21" height="15" viewBox="0 0 21 15">
        <g fill="var(--icon-idle)"><rect width="21" height="2" rx="1"/><rect y="6.5" width="17" height="2" rx="1"/><rect y="13" width="14" height="2" rx="1"/></g>
      </svg>
      <h1>Conversations</h1>
      <svg class="search-icon" width="16" height="16" viewBox="0 0 16 16">
        <circle cx="6.5" cy="6.5" r="5" fill="none" stroke="var(--icon-idle)" stroke-width="2"/>
        <line x1="10.2" y1="10.2" x2="15" y2="15" stroke="var(--icon-idle)" stroke-width="2.4" stroke-linecap="round"/>
      </svg>
    </header>

    <ul class="conversation-list">
      <li class="conversation">
        <div class="avatar" role="img" aria-label="Profile photo of Theo Varnell" style="background:linear-gradient(135deg,#3c4a2e,#b98a6a)"></div>
        <div><p class="contact-name">Theo Varnell</p><p class="last-message"><span class="status status--online"></span>Hello is this working</p></div>
      </li>
      <li class="conversation">
        <div class="avatar" role="img" aria-label="Profile photo of Ansel Dorring" style="background:linear-gradient(135deg,#6f7a5a,#3a3f44)"></div>
        <div><p class="contact-name">Ansel Dorring</p><p class="last-message"><span class="status status--away"></span>This is the guide then any one could use it</p></div>
      </li>
      <li class="conversation">
        <div class="avatar" role="img" aria-label="Profile photo of Lucia Fenwick" style="background:linear-gradient(135deg,#3a1e18,#c99a86)"></div>
        <div><p class="contact-name">Lucia Fenwick</p><p class="last-message"><span class="status status--online"></span>Hello is this working</p></div>
      </li>
      <li class="conversation">
        <div class="avatar" role="img" aria-label="Profile photo of Maren Holt" style="background:linear-gradient(135deg,#e8cfa8,#d8866c)"></div>
        <div><p class="contact-name">Maren Holt</p><p class="last-message"><span class="status status--away"></span>This is the guide then any one could us..</p></div>
      </li>
      <li class="conversation">
        <div class="avatar avatar--placeholder">
          <svg width="18" height="20" viewBox="0 0 18 20"><g fill="#fff"><circle cx="9" cy="5" r="4.5"/><path d="M0 20c0-6 4-9 9-9s9 3 9 9z"/></g></svg>
        </div>
        <div><p class="contact-name">Lucia Fenwick</p><p class="last-message"><span class="status status--online"></span>I wish you an amazing time this time argenti.</p></div>
      </li>
      <li class="conversation">
        <div class="avatar" role="img" aria-label="Profile photo of Dorian Holt" style="background:linear-gradient(135deg,#2a2420,#e6c6a6)"></div>
        <div><p class="contact-name">Dorian Holt</p><p class="last-message"><span class="status status--busy"></span>This is the guide then any one could us..</p></div>
      </li>
    </ul>

    <nav class="tab-bar">
      <svg width="19" height="18" viewBox="0 0 19 18" aria-label="Conversations">
        <g fill="var(--icon-active)"><path d="M0 1a1 1 0 0 1 1-1h11a1 1 0 0 1 1 1v8a1 1 0 0 1-1 1H4l-4 3z"/><path d="M14.5 4H18a1 1 0 0 1 1 1v13l-4-3H6a1 1 0 0 1-1-1v-2.5h8.5a1 1 0 0 0 1-1z"/></g>
      </svg>
      <svg width="16" height="16" viewBox="0 0 16 16" aria-label="Dashboard">
        <g fill="var(--icon-idle)"><rect width="7.3" height="7.3"/><rect x="8.7" width="7.3" height="7.3"/><rect y="8.7" width="7.3" height="7.3"/><rect x="8.7" y="8.7" width="7.3" height="7.3"/></g>
      </svg>
      <svg width="16" height="16" viewBox="0 0 16 16" aria-label="Contacts">
        <rect width="16" height="16" rx="2" fill="var(--icon-idle)"/>
        <circle cx="8" cy="6" r="2.6" fill="#fff"/><path d="M3.5 13c0-3 2-4.3 4.5-4.3s4.5 1.3 4.5 4.3z" fill="#fff"/>
      </svg>
      <svg width="20" height="18" viewBox="0 0 20 18" aria-label="Map">
        <path d="M10 0a5 5 0 0 1 5 5c0 3.5-5 8.5-5 8.5S5 8.5 5 5a5 5 0 0 1 5-5z" fill="var(--icon-idle)"/>
        <circle cx="10" cy="5" r="1.9" fill="#fff"/>
        <path d="M3 12h3.5l3.5 3 3.5-3H17l3 6H0z" fill="var(--icon-idle)"/>
      </svg>
      <svg width="18" height="18" viewBox="0 0 18 18" aria-label="Settings">
        <g fill="var(--icon-idle)" transform="translate(9 9)">
          <circle r="6"/>
          <rect x="-1.8" y="-9" width="3.6" height="18" rx="1"/>
          <rect x="-1.8" y="-9" width="3.6" height="18" rx="1" transform="rotate(45)"/>
          <rect x="-1.8" y="-9" width="3.6" height="18" rx="1" transform="rotate(90)"/>
          <rect x="-1.8" y="-9" width="3.6" height="18" rx="1" transform="rotate(135)"/>
        </g>
        <circle cx="9" cy="9" r="2.6" fill="#fff"/>
      </svg>
    </nav>
  </main>
</body>
</html>
```